Pelkman Agency (http://pa.quorvexstudio.com/)

We are looking for a similar design to what we have, but more professional looking and cleaned up with links and logo that is not so grainy looking. We are an independent insurance agency marketing to personal and commercial clients. We offer all commercial lines markets and all personal lines. We target excavators, landscapers, restaurants, golf courses, contractors. Please look at http://pa.quorvexstudio.com/ which we had designed but do not like it, it will give you an idea of what we are looking for.

Target Market(s)

Commercial and personal insurance. All business products and all personal (homeowners, auto, antique auto, umbrella)

Industry/Entity Type

It Professional

Logo Text

Knowledge Building Your Assurance

Number of Pages Required

5+ page

Colors
000000
848484
0255a3

```html
<!DOCTYPE html>
<html lang="en">
<head>
<meta charset="utf-8">
<title>Pelkman Agency – Insurance Services</title>
<link rel="stylesheet" href="https://fonts.googleapis.com/css2?family=Didact+Gothic&family=Open+Sans:wght@400;600&display=swap">
<style>
:root{
  --blue:#0255a3;
  --blue-dark:#034a8d;
  --black:#000000;
  --grey:#848484;
  --grey-light:#c9c9c9;
  --panel:#f1f1f1;
  --text:#222222;
  --white:#ffffff;
}
*{box-sizing:border-box;margin:0;padding:0}
html,body{width:972px;height:1200px;overflow:hidden;background:var(--white)}
body{position:relative;font-family:"Didact Gothic",sans-serif;color:var(--text)}
a{color:inherit;text-decoration:none}

.site-header{position:absolute;left:0;top:0;width:972px;height:75px;background:var(--white)}
.brand{position:absolute;left:127px;top:30px;display:flex;align-items:center;gap:7px}
.brand-mark{width:12px;height:12px;background:var(--blue)}
.brand-name{font-family:"Didact Gothic",sans-serif;font-size:19px;color:var(--blue);letter-spacing:.3px}
.header-call{position:absolute;left:553px;top:16px;font-family:"Open Sans",sans-serif;font-size:10.5px;color:var(--grey);display:flex;align-items:center;gap:5px}
.header-call strong{color:var(--blue);font-weight:600}
.quote-btn{position:absolute;left:735px;top:12px;width:110px;height:22px;background:var(--blue);color:var(--white);font-family:"Open Sans",sans-serif;font-size:9.5px;font-weight:600;display:flex;align-items:center;justify-content:center;gap:5px;border-radius:2px}
.main-nav{position:absolute;left:351px;top:56px;display:flex;gap:0;font-family:"Open Sans",sans-serif;font-size:8.5px;color:var(--grey);letter-spacing:.2px}
.main-nav a{margin-right:24px}
.main-nav a:last-child{margin-right:0}
.main-nav .active{color:var(--blue)}

.hero{position:absolute;left:0;top:75px;width:972px;height:362px;background:linear-gradient(100deg,#e9e9e9 0%,#bdbdbd 25%,#9a9a9a 45%,#d4d4d4 62%,#5a5a5a 80%,#3c3c3c 100%)}
.tagline-band{position:absolute;left:0;top:437px;width:972px;height:71px;background:var(--blue);color:var(--white);font-family:"Didact Gothic",sans-serif;font-size:24px;display:flex;align-items:center;justify-content:center;letter-spacing:.2px}
.band-pointer{position:absolute;left:457px;top:507px}

.intro{position:absolute;left:0;top:565px;width:972px;text-align:center;font-size:21px;line-height:28px;color:var(--grey)}

.coverage{position:absolute;top:657px;width:170px;height:217px;text-align:center}
.coverage svg{position:absolute;left:34px;top:2px}
.coverage-label{position:absolute;left:0;width:170px;top:151px;font-size:17px;color:var(--black)}
.coverage.featured{background:var(--blue)}
.coverage.featured svg{top:26px}
.coverage.featured .coverage-label{top:176px;color:var(--white)}

.footer-divider{position:absolute;left:0;top:916px;width:972px;height:1px;background:var(--grey-light)}
.resource{position:absolute;left:128px;width:262px;height:68px}
.resource-box{position:absolute;left:60px;top:7px;width:201px;height:57px;background:var(--panel);border:1px solid #e0e0e0;border-radius:2px;padding:11px 0 0 19px;font-size:13.5px;line-height:17px;color:var(--text)}
.resource-icon{position:absolute;left:0;top:0;width:72px;height:72px;border-radius:50%;background:var(--white);border:1px solid #e4e4e4;display:flex;align-items:center;justify-content:center}
.resource-icon span{width:60px;height:60px;border-radius:50%;display:flex;align-items:center;justify-content:center}
.slash{position:absolute;left:438px;top:948px}

.contact{position:absolute;left:584px;top:953px;font-family:"Open Sans",sans-serif;font-size:9.5px;line-height:15px;color:var(--text)}
.contact .muted{color:var(--grey)}
.contact .link{color:var(--blue)}
.contact .u{color:var(--blue);text-decoration:underline}
.contact-row{display:flex;margin-top:9px}
.contact-row dt{width:66px}
.follow{display:flex;align-items:center;gap:9px;margin-top:12px}
.follow i{display:block;width:17px;height:17px;background:var(--grey);border-radius:3px}

.site-footer{position:absolute;left:0;top:1163px;width:972px;height:37px;background:var(--black);color:#bdbdbd;font-family:"Open Sans",sans-serif;font-size:9.5px}
.footer-links{position:absolute;left:127px;top:12px}
.footer-links span{margin:0 6px}
.copyright{position:absolute;right:127px;top:12px}
</style>
</head>
<body>

<header class="site-header">
  <a class="brand" href="#"><span class="brand-mark"></span><span class="brand-name">Pelkman Agency</span></a>
  <div class="header-call">
    <svg width="9" height="9" viewBox="0 0 24 24"><path fill="#848484" d="M6.6 10.8a15 15 0 0 0 6.6 6.6l2.2-2.2c.3-.3.7-.4 1-.2 1.1.4 2.3.6 3.6.6.6 0 1 .4 1 1V20c0 .6-.4 1-1 1A17 17 0 0 1 3 4c0-.6.4-1 1-1h3.5c.6 0 1 .4 1 1 0 1.3.2 2.5.6 3.6.1.3 0 .7-.2 1z"/></svg>
    Call us today - <strong>1-888-4 PELKMN</strong>
  </div>
  <a class="quote-btn" href="#">
    <svg width="9" height="9" viewBox="0 0 24 24"><path fill="none" stroke="#fff" stroke-width="3" d="M4 6h9M4 6v14h14v-8"/><path fill="#fff" d="M10 14l1-4 9-9 3 3-9 9z"/></svg>
    GET A FREE QUOTE
  </a>
  <nav class="main-nav">
    <a class="active" href="#">HOME</a>
    <a href="#">ABOUT US</a>
    <a href="#">PERSONAL INSURANCE</a>
    <a href="#">BUSINESS INSURANCE</a>
    <a href="#">SERVICE CENTER</a>
    <a href="#">CONTACT US</a>
  </nav>
</header>

<div class="hero" role="img" aria-label="Black and white photo of an insurance agent meeting with a smiling couple at a table"></div>

<div class="tagline-band">SMALL ENOUGH TO CARE, BIG ENOUGH TO MAKE A DIFFERENCE</div>
<svg class="band-pointer" width="58" height="20" viewBox="0 0 58 20"><path d="M0 0h58L29 20z" fill="#0255a3"/></svg>

<p class="intro">Please find information about our agency, its principles, and<br>the various types of insurance coverages that we provide.</p>

<a class="coverage" href="#" style="left:128px">
  <svg width="110" height="125" viewBox="0 0 110 125"><path d="M55 4C40 12 22 14 6 11c-4 28-2 55 10 75 10 16 24 27 39 34 15-7 29-18 39-34 12-20 14-47 10-75-16 3-34 1-49-7z" fill="none" stroke="#c9c9c9" stroke-width="3"/>
    <g fill="#0255a3"><rect x="33" y="40" width="3" height="40"/><rect x="33" y="77" width="46" height="3"/><rect x="40" y="64" width="6" height="12"/><rect x="49" y="56" width="6" height="20"/><rect x="58" y="52" width="6" height="24"/><rect x="67" y="46" width="6" height="30"/><path d="M38 60l12-10 8 5 14-14" fill="none" stroke="#0255a3" stroke-width="3"/><path d="M68 38h8v8z"/></g></svg>
  <span class="coverage-label">Business Insurance</span>
</a>

<a class="coverage featured" href="#" style="left:310px">
  <svg width="110" height="125" viewBox="0 0 110 125"><path d="M55 4C40 12 22 14 6 11c-4 28-2 55 10 75 10 16 24 27 39 34 15-7 29-18 39-34 12-20 14-47 10-75-16 3-34 1-49-7z" fill="none" stroke="#fff" stroke-width="3"/>
    <g fill="#fff"><path d="M36 48h38l6 12h3v18h-6v6h-8v-6H44v6h-8v-6h-6V60h3z"/></g>
    <g fill="#0255a3"><path d="M39 52h32l4 8H35z"/><circle cx="40" cy="68" r="3.5"/><circle cx="70" cy="68" r="3.5"/><rect x="47" y="66" width="16" height="4"/></g></svg>
  <span class="coverage-label">Auto Insurance</span>
</a>

<a class="coverage" href="#" style="left:492px">
  <svg width="110" height="125" viewBox="0 0 110 125"><path d="M55 4C40 12 22 14 6 11c-4 28-2 55 10 75 10 16 24 27 39 34 15-7 29-18 39-34 12-20 14-47 10-75-16 3-34 1-49-7z" fill="none" stroke="#c9c9c9" stroke-width="3"/>
    <g fill="#0255a3"><circle cx="55" cy="42" r="9"/><rect x="44" y="53" width="22" height="18" rx="4"/><rect x="34" y="55" width="10" height="6" rx="3"/><rect x="66" y="55" width="10" height="6" rx="3"/><path d="M44 71h9l-6 14h-9zM57 71h9l6 14h-9z"/></g></svg>
  <span class="coverage-label">Life Insurance</span>
</a>

<a class="coverage" href="#" style="left:677px">
  <svg width="110" height="125" viewBox="0 0 110 125"><path d="M55 4C40 12 22 14 6 11c-4 28-2 55 10 75 10 16 24 27 39 34 15-7 29-18 39-34 12-20 14-47 10-75-16 3-34 1-49-7z" fill="none" stroke="#c9c9c9" stroke-width="3"/>
    <g fill="#0255a3"><path d="M30 58l22-20 26 20h-4l-22-17-18 17z"/><path d="M36 58l16-14 20 14v24H36z"/></g>
    <g fill="#fff"><rect x="41" y="60" width="6" height="6"/><rect x="41" y="70" width="6" height="6"/><rect x="53" y="60" width="6" height="6"/><rect x="63" y="60" width="6" height="6"/><rect x="63" y="70" width="6" height="6"/><rect x="53" y="70" width="6" height="12"/></g></svg>
  <span class="coverage-label">Home Insurance</span>
</a>

<div class="footer-divider"></div>

<a class="resource" href="#" style="top:957px">
  <div class="resource-box">Personal and Business<br>Insurance Services Guide</div>
  <div class="resource-icon"><span style="background:#3a3a3a">
    <svg width="26" height="30" viewBox="0 0 26 30"><rect x="3" y="2" width="20" height="26" rx="2" fill="none" stroke="#fff" stroke-width="2"/><path d="M8 10h10M8 15h10M8 20h7" stroke="#fff" stroke-width="2"/></svg>
  </span></div>
</a>

<a class="resource" href="#" style="top:1051px">
  <div class="resource-box">Request a Free<br>Insurance Services Quote</div>
  <div class="resource-icon"><span style="background:var(--blue)">
    <svg width="34" height="26" viewBox="0 0 34 26"><rect x="2" y="6" width="30" height="18" fill="none" stroke="#fff" stroke-width="2"/><path d="M2 6l15 11 15-11" fill="none" stroke="#fff" stroke-width="2"/><path d="M9 2h16v8H9z" fill="#fff"/><path d="M12 5h10" stroke="#0255a3" stroke-width="1.5"/></svg>
  </span></div>
</a>

<svg class="slash" width="96" height="186" viewBox="0 0 96 186"><path d="M93 1L2 185" stroke="#bdbdbd" stroke-width="1"/></svg>

<div class="contact">
  <p class="muted">For your convenience please feel free to<br>reach us by email at: <a class="link" href="#">admin@pelkmanagency.com</a></p>
  <p style="margin-top:9px">Call us Now! <span class="link">1-888-4 Pelkman</span></p>
  <dl class="contact-row"><dt>Office Phone:</dt><dd><span class="u">908-555-0142 (Alder Ridge),</span><br><span class="u">(609) 555-0187 (Bayport)</span></dd></dl>
  <dl class="contact-row"><dt>Office Fax:</dt><dd><span class="u">908-555-0163 (Alder Ridge),</span><br><span class="u">(609) 555-0129 (Bayport)</span></dd></dl>
  <div class="follow">Follow Us on: <i></i><i></i><i></i><i></i><i></i></div>
</div>

<footer class="site-footer">
  <div class="footer-links"><a href="#">Home</a><span>|</span><a href="#">Personal Insurance</a><span>|</span><a href="#">Business Insurance</a><span>|</span><a href="#">Service Center</a><span>|</span><a href="#">About US</a><span>|</span> <a href="#">Contact Us</a></div>
  <div class="copyright">© 2015 Pelkman Agency. All Rights Reserved</div>
</footer>

</body>
</html>
```